Quendra - Clear Spirit Cosmetics

Please design a logo and business cards for new food supplements, cosmetics and herbal fixatives. The products are produced ecologically and biologically in the South Tyrol and Trentino alps. The products are pure and noble. Quendra = pure vitality Colors Background: dark or black matt (soft touch) Logodesign: powerful, elegant, violet with glossy foil The logo and design should convey warmth, passion and the 6th sense, you should get the impression that you can smell the herbal odor , Logo and business cards for new food supplements, cosmetics and herbal fixatives. The products are produced ecologically and biologically in the South Tyrol and Trentino alps. The products are pure and noble. Quendra = pure vitality Colors Background: dark or black matt (softtouch) Logodesign: powerful elegant violet with glossy foil The logo and design is meant to convey warmth, passion and the 6th sense, you should get the impression that you can smell the herbal perfume.

Target Market(s)

Food, food supplements, vitality, health

Contact Information for Business Card

Please provide an elegant darf design that is puristic, but has a very good logo design
Elegantes dunkles design, puristisch

Logo Text

Quendra - clear Spirit

Colors
6b449b

Requirements
Must have
• SVG Files Alpha channel for foil embossing High-quality design
Nice to have
• Pure elegance
Should not have
• to colorful colors

```html
<!DOCTYPE html>
<html lang="de">
<head>
<meta charset="utf-8">
<title>Quendra – Visitenkarten</title>
<link rel="stylesheet" href="https://fonts.googleapis.com/css2?family=Open+Sans:wght@300;400&display=swap">
<style>
  :root {
    --backdrop: #2a2a2a;
    --card: #222123;
    --card-edge: #2c2b2e;
    --violet: #6b449b;
    --silver: #c9c9cc;
    --silver-dim: #a7a7ab;
    --faint-ring: rgba(255,255,255,0.035);
  }
  * { box-sizing: border-box; margin: 0; padding: 0; }
  html, body { width: 1200px; height: 600px; overflow: hidden; }
  body {
    background: var(--backdrop);
    font-family: "Open Sans", sans-serif;
    position: relative;
  }
  .card {
    position: absolute;
    width: 465px;
    height: 272px;
    border-radius: 18px;
    background: var(--card);
    border: 1px solid var(--card-edge);
    overflow: hidden;
  }
  .card--back  { left: 123px; top: 165px; }
  .card--front { left: 613px; top: 164px; }
  .backdrop-ring {
    position: absolute;
    border-radius: 50%;
    border: 22px solid var(--faint-ring);
  }
  .card--back .backdrop-ring  { width: 230px; height: 230px; left: 175px; top: 30px; }
  .card--front .backdrop-ring { width: 230px; height: 230px; left: 115px; top: 30px; }
  .brand {
    position: absolute;
    text-align: center;
    transform: translateX(-50%);
  }
  .brand__mark {
    display: block;
    margin: 0 auto;
    border-radius: 50%;
    border: 3px solid var(--silver);
  }
  .brand__name {
    display: block;
    color: var(--silver);
    font-weight: 400;
    line-height: 1;
  }
  .brand__tagline {
    display: block;
    color: var(--violet);
    text-transform: uppercase;
    line-height: 1;
  }
  .card--back .brand { left: 131px; top: 76px; }
  .card--back .brand__mark { width: 62px; height: 62px; }
  .card--back .brand__name { font-size: 29px; margin-top: 18px; letter-spacing: 0.5px; }
  .card--back .brand__tagline { font-size: 8px; letter-spacing: 3.4px; margin-top: 5px; }
  .card--front .brand { left: 224px; top: 70px; }
  .card--front .brand__mark { width: 68px; height: 68px; }
  .card--front .brand__name { font-size: 44px; margin-top: 18px; letter-spacing: 1px; }
  .card--front .brand__tagline { font-size: 10px; letter-spacing: 5px; margin-top: 6px; }
  .contact {
    position: absolute;
    left: 268px;
    top: 82px;
  }
  .contact__name { font-size: 18px; font-weight: 300; color: var(--silver); line-height: 1.1; }
  .contact__role { font-size: 11px; color: var(--violet); margin-top: 2px; }
  .contact__list { list-style: none; margin-top: 22px; }
  .contact__item {
    display: flex; align-items: center; gap: 6px;
    font-size: 12.5px; color: var(--silver-dim); font-weight: 300;
    height: 24px;
  }
  .contact__icon { width: 12px; height: 12px; fill: var(--violet); }
</style>
</head>
<body>
  <section class="card card--back">
    <div class="backdrop-ring"></div>
    <div class="brand">
      <span class="brand__mark"></span>
      <span class="brand__name">QUENDRA</span>
      <span class="brand__tagline">Clear Spirit</span>
    </div>
    <div class="contact">
      <p class="contact__name">Dein Name</p>
      <p class="contact__role">Berufsbezeichnung</p>
      <ul class="contact__list">
        <li class="contact__item">
          <svg class="contact__icon" viewBox="0 0 12 12" aria-hidden="true"><path d="M1 4c0-2 2-3 5-3s5 1 5 3l-2 1-1-1.5H4L3 5zM3 6h6l1.5 4.5h-9z"/></svg>
          000 000 0000
        </li>
        <li class="contact__item">
          <svg class="contact__icon" viewBox="0 0 12 12" aria-hidden="true"><path d="M0 2.5h12v7H0z"/><path d="M0.5 3l5.5 4 5.5-4" fill="none" stroke="#222123" stroke-width="1"/></svg>
          name@quendra-mail.com
        </li>
      </ul>
    </div>
  </section>

  <section class="card card--front">
    <div class="backdrop-ring"></div>
    <div class="brand">
      <span class="brand__mark"></span>
      <span class="brand__name">QUENDRA</span>
      <span class="brand__tagline">Clear Spirit</span>
    </div>
  </section>
</body>
</html>
```